Web Design Project for Film Business

We need a web design for a new company based in Bondi Beach, Sydney, Australia. We basically provide filming and video editing services. Our targets are basically corporate videos, wedding videos and other types of functions.
The important thing to know about us is that we are not just people that press the record button, we consider ourselves story tellers. We can make something boring like a conference look interesting to watch and we can also make a wedding look like a blockbuster movie that you can't look away from until its finished.
We need something as new and fresh as Bondi Beach. A young place where people come from all over the world to enjoy summer and we are lucky to be based here.
To see some of our work please visit our clipnest Channel. Make sure you watch a couple of wedding video and the corporate video so you can have a better understanding about our style.
Please note- we are not trying to market ourselves exclusively as wedding videographers, nor do we want to exploit the idea of the beach.

http://clipnest.example/channels/518374

sites that we really like:

http://www.quillharbour.example.co.uk/
http://www.fennwixley.example.co.uk/

Target Market(s)

Couples - Corporate

Industry/Entity Type

Business

Requirements
Must have
• 5 to 6 pages (we are still deciding)
-main page
-our story (story about Tarrow Films)
-your story (page designated for wedding videos)
-your business (page designated for corporate videos)
-contact us
-other stuff
Nice to have
• I would like to see some animation. Maybe you can animate our logo. Up to the designer

```html
<!DOCTYPE html>
<html lang="en">
<head>
<meta charset="utf-8">
<title>Tarrow Films</title>
<link rel="stylesheet" href="https://fonts.googleapis.com/css2?family=Oswald:wght@500&family=Josefin+Sans:wght@300&family=Rubik+Dirt&family=PT+Sans:wght@400;700&family=Gelasio:ital@1&family=Open+Sans:wght@400&display=swap">
<style>
:root{
  --bg:#1d1d1d;
  --bg-top:#2e2e2e;
  --ink:#0c0c0c;
  --red:#d8263a;
  --brush-red:#e0283f;
  --cyan:#35c9c1;
  --gold:#e0a11e;
  --orange:#e08a1e;
  --text:#9a9a9a;
  --rule:#3a3a3a;
  --footer:#141414;
}
*{margin:0;padding:0;box-sizing:border-box}
html,body{width:1000px;height:1200px;overflow:hidden}
body{
  position:relative;
  background:
    radial-gradient(ellipse 520px 360px at 500px 120px,#3a3a3a 0%,rgba(0,0,0,0) 100%),
    linear-gradient(180deg,var(--bg-top) 0,var(--bg) 520px,var(--bg) 100%);
  font-family:"PT Sans",sans-serif;
  color:var(--text);
}
.abs{position:absolute}
.brand{left:0;width:1000px;top:36px;text-align:center;font-family:"Oswald",sans-serif;font-weight:500;font-size:40px;letter-spacing:2px;color:var(--orange);line-height:48px}
.hero{left:55px;top:112px}
.main-nav{left:187px;top:131px;width:626px;height:38px;border-radius:19px;
  background:linear-gradient(180deg,rgba(70,55,45,.85),rgba(20,15,12,.9));
  box-shadow:0 0 0 1px rgba(0,0,0,.6),inset 0 1px 0 rgba(255,255,255,.15);
  display:flex;justify-content:space-evenly;align-items:center;padding:0 14px}
.main-nav a{font-family:"Oswald",sans-serif;font-weight:500;font-size:18px;color:#f2f2f2;text-decoration:none;letter-spacing:.5px}
.section-title{font-family:"Josefin Sans",sans-serif;font-weight:300;font-size:16.5px;color:var(--red);text-transform:uppercase;line-height:20px}
.project{width:162px}
.project .thumb{width:160px;height:124px;border:4px solid #4b4b4b;background:#333;margin-top:30px;box-shadow:0 2px 6px rgba(0,0,0,.6)}
.project .thumb div{width:100%;height:100%}
.project h3{font-weight:400;font-size:13px;color:var(--cyan);margin-top:14px;line-height:16px}
.project .by{font-size:11px;color:#888;line-height:13px}
.project ul{list-style:none;margin-top:4px;border-top:1px dotted var(--rule)}
.project li{font-size:11px;line-height:16px;border-bottom:1px dotted var(--rule);padding-left:1px;color:#8d8d8d}
.more{font-size:11px;color:#aaa;margin-top:4px}
.more b{color:#e6e6e6;font-weight:400}
.more span{color:#666}
.welcome-small{font-family:"Josefin Sans",sans-serif;font-weight:300;font-size:24px;color:var(--red);line-height:30px}
.welcome-name{font-family:"Rubik Dirt",sans-serif;font-size:22px;color:var(--cyan);line-height:28px;text-transform:uppercase}
.welcome-body{left:552px;top:617px;width:384px;font-size:10.5px;line-height:14.9px;color:var(--text)}
.question-title{font-family:"Rubik Dirt",sans-serif;font-size:24px;color:var(--cyan);letter-spacing:2px}
.contact-label{font-size:11px;color:#eee}
.contact-value{font-family:"Open Sans",sans-serif;font-size:16px;color:var(--cyan);white-space:nowrap}
.social{height:28px;background:var(--brush-red);display:flex;align-items:center;gap:7px;padding:0 10px;
  font-family:"PT Sans",sans-serif;font-weight:700;font-size:13px;color:#fff;
  clip-path:polygon(3% 8%,97% 0,100% 50%,96% 100%,2% 92%,0 50%)}
.social i{display:block;width:16px;height:16px;background:#fff;border-radius:2px}
.share{font-family:"Rubik Dirt",sans-serif;font-size:17px;color:var(--red);line-height:19px;letter-spacing:1px}
.happy{font-family:"Open Sans",sans-serif;font-size:17px;color:var(--gold)}
.quote-mark{font-family:"Gelasio",serif;font-style:italic;font-size:110px;color:#3c3c3c;line-height:1}
.testimonial{left:583px;top:957px;width:305px;font-family:"Gelasio",serif;font-style:italic;font-size:12.4px;line-height:16.6px;color:#a3a3a3}
.site-footer{left:0;top:1152px;width:1000px;height:48px;background:var(--footer);border-top:1px solid #252525}
.footer-brand{left:708px;top:1163px;font-family:"Oswald",sans-serif;font-weight:500;font-size:11px;line-height:12px;color:#555;width:50px;text-align:center}
.copyright{left:768px;top:1169px;font-size:10px;color:#6a6a6a}
</style>
</head>
<body>

<header>
  <div class="abs brand">TARROW FILMS</div>

  <svg class="abs hero" width="890" height="410" viewBox="0 0 890 410" role="img" aria-label="Wedding reception photograph: bride and groom walking through applauding guests in a warmly lit ballroom">
    <defs>
      <linearGradient id="heroFill" x1="0" y1="0" x2="0" y2="1">
        <stop offset="0" stop-color="#5a3e2a"/>
        <stop offset=".45" stop-color="#3a2a22"/>
        <stop offset="1" stop-color="#1c1614"/>
      </linearGradient>
      <radialGradient id="heroGlow" cx=".5" cy=".55" r=".35">
        <stop offset="0" stop-color="#c9b8a8" stop-opacity=".45"/>
        <stop offset="1" stop-color="#c9b8a8" stop-opacity="0"/>
      </radialGradient>
      <linearGradient id="frameFill" x1="0" y1="0" x2="0" y2="1">
        <stop offset="0" stop-color="#2a2a2a"/>
        <stop offset="1" stop-color="#0e0e0e"/>
      </linearGradient>
    </defs>
    <path d="M0 12 Q445 -40 890 12 L890 388 Q445 300 0 388 Z" fill="url(#frameFill)"/>
    <path d="M14 20 Q445 -26 877 20 L877 372 Q445 292 14 372 Z" fill="url(#heroFill)"/>
    <path d="M14 20 Q445 -26 877 20 L877 372 Q445 292 14 372 Z" fill="url(#heroGlow)"/>
  </svg>

  <nav class="abs main-nav">
    <a href="#">HOME</a><a href="#">WHO</a><a href="#">BLOG</a><a href="#">PORTFOLIO</a><a href="#">PHOTOS</a><a href="#">PROJECTS</a><a href="#">CONTACT</a>
  </nav>
</header>

<main>
  <section class="abs project" style="left:75px;top:537px">
    <h2 class="section-title">Fresh Projects</h2>
    <div class="thumb"><div role="img" aria-label="Couple on a seaside boardwalk" style="background:linear-gradient(180deg,#b9c3c9 0,#8e9aa0 45%,#6a6c66 100%)"></div></div>
    <h3>Liam+Sera</h3>
    <p class="by">by Maren Tollis</p>
    <ul><li>Lorem ipsum dolor</li><li>Lorem ipsum dolor</li><li>Lorem ipsum dolor</li><li>Lorem ipsum dolor</li></ul>
    <p class="more">See <b>Project</b> <span>+</span></p>
  </section>

  <section class="abs project" style="left:336px;top:537px">
    <h2 class="section-title">Latest Work</h2>
    <div class="thumb"><div role="img" aria-label="Speaker on stage at a conference" style="background:linear-gradient(180deg,#1c2040 0,#2a2f55 50%,#3c3a36 100%)"></div></div>
    <h3>Ardent National Con</h3>
    <p class="by">by Maren Tollis</p>
    <ul><li>Lorem ipsum dolor</li><li>Lorem ipsum dolor</li><li>Lorem ipsum dolor</li><li>Lorem ipsum dolor</li></ul>
    <p class="more">See <b>Portfolio</b> <span>+</span></p>
  </section>

  <section>
    <div class="abs" style="left:550px;top:538px">
      <h2 class="welcome-small">WELCOME TO</h2>
      <p class="welcome-name">Tarrow Films</p>
    </div>
    <div class="abs" style="left:550px;top:605px;width:385px;border-top:1px dotted #444"></div>
    <p class="abs welcome-body">Lorem ipsum dolor sit amet, consectetur adipisicing elit, sed do eiusmod tempor incididunt ut labore et dolore magna aliqua. Ut enim ad minim veniam, quis nostrud exercitation ullamco laboris nisi ut aliquip ex ea commodo consequat. Duis aute irure dolor in reprehenderit in voluptate velit esse cillum dolore eu fugiat nulla pariatur. Excepteur sint occaecat cupidatat non proident, sunt in culpa qui officia deserunt mollit anim id est laborum. Lorem ipsum dolor sit amet, consectetur adipisicing elit, sed do eiusmod tempor incididunt ut labore et dolore magna aliqua. Ut enim ad minim veniam, quis nostrud exercitation ullamco laboris nisi ut aliquip ex ea commodo consequat. Duis aute irure dolor in reprehenderit in voluptate velit esse cillum dolore eu fugiat nulla pariatur. Excepteur sint occaecat cupidatat non proident, sunt in culpa qui officia deserunt mollit anim id est laborum. fugiat nulla pariatur. Excepteur sint occaecat cupidatat non proident, sunt in culpa qui officia deserunt mollit anim id est laborum.</p>
    <p class="abs more" style="left:552px;top:828px">Read <b>More</b> <span>+</span></p>
  </section>

  <section class="contact-box">
    <svg class="abs" style="left:44px;top:880px" width="445" height="112" viewBox="0 0 445 112" aria-hidden="true">
      <path d="M4 6 L216 2 L220 20 L214 52 L100 56 L92 108 L438 106 L442 88 L436 54 L222 52 L218 58 L6 56 L2 30 Z" fill="var(--ink)"/>
      <path d="M92 50 L440 50 L444 80 L438 108 L92 108 Z" fill="var(--ink)"/>
    </svg>
    <p class="abs question-title" style="left:63px;top:895px">QUESTION?</p>
    <div class="abs" style="left:153px;top:940px">
      <p class="contact-label">Call us</p>
      <p class="contact-value">1-888-555-0192</p>
    </div>
    <div class="abs" style="left:308px;top:940px">
      <p class="contact-label">Email us</p>
      <p class="contact-value">info@tarrow.example</p>
    </div>
  </section>

  <section class="share-links">
    <div class="abs" style="left:192px;top:1032px;width:148px;height:66px;background:var(--ink)"></div>
    <p class="abs share" style="left:220px;top:1048px">SHARE<br>WITH US</p>
    <a class="abs social" style="left:80px;top:1025px;width:112px"><i></i>Chatterly</a>
    <a class="abs social" style="left:80px;top:1058px;width:118px"><i></i>Friendwall</a>
    <a class="abs social" style="left:88px;top:1092px;width:120px"><i></i>Snapfolio</a>
    <a class="abs social" style="left:330px;top:1021px;width:116px;justify-content:flex-end">Clipnest<i></i></a>
    <a class="abs social" style="left:334px;top:1055px;width:118px;justify-content:flex-end">Placehop<i></i></a>
    <a class="abs social" style="left:338px;top:1087px;width:108px;justify-content:flex-end">Shotboard<i></i></a>
  </section>

  <section class="testimonial-box">
    <svg class="abs" style="left:533px;top:878px" width="376" height="62" viewBox="0 0 376 62" aria-hidden="true">
      <g stroke="#3a3a3a" stroke-width="1">
        <line x1="0" y1="16" x2="376" y2="16"/><line x1="0" y1="26" x2="376" y2="26"/><line x1="0" y1="36" x2="376" y2="36"/>
      </g>
      <path d="M40 4 L340 2 L344 30 L338 56 L150 60 L72 58 L44 56 L38 30 Z" fill="var(--ink)"/>
    </svg>
    <p class="abs happy" style="left:533px;top:894px;width:376px;text-align:center">I Make My Clients Happy!</p>
    <span class="abs quote-mark" style="left:530px;top:918px">“</span>
    <span class="abs quote-mark" style="left:884px;top:1072px">”</span>
    <p class="abs testimonial">Lorem ipsum dolor sit amet, consectetur adipisicing elit, sed do eiusmod tempor incididunt ut labore et dolore magna aliqua. Ut enim ad minim veniam, quis nostrud exercitation ullamco laboris nisi ut aliquip ex ea commodo consequat. Duis aute irure dolor in reprehenderit in voluptate velit esse cillum dolore eu fugiat nulla pariatur. Excepteur sint occaecat cupidatat non proident, sunt in culpa qui officia deserunt mollit anim id est laborum.</p>
  </section>
</main>

<footer>
  <div class="abs site-footer"></div>
  <p class="abs footer-brand">TARROW<br>FILMS</p>
  <p class="abs copyright">©2011 Tarrow Films. All rights reserved.</p>
</footer>

</body>
</html>
```